Endocrinologist needs new stationery

I have a logo from ArtHiveLab and now need stationery with the new logo.

Address: Suite 4, 238 Kestrel Lane, Richmond, VIC 3121
Phone: 03 9412 7053
Fax: 03 9412 7055
Website: www.drmelvaparkson.com.au
Email: admin@drmelvaparkson.com.au

```html
<!DOCTYPE html>
<html lang="en">
<head>
<meta charset="utf-8">
<title>Dr Melva Parkson – Stationery</title>
<link href="https://fonts.googleapis.com/css2?family=Open+Sans:wght@400;600;700&family=Arimo:wght@400&display=swap" rel="stylesheet">
<style>
  :root {
    --backdrop: #e3e3e3;
    --paper: #ffffff;
    --brand-blue: #336a9c;
    --brand-plum: #744f66;
    --ink: #4a4a4a;
    --ink-soft: #5a5a5a;
    --rule: #7a7a7a;
  }
  html, body { margin: 0; padding: 0; overflow: hidden; }
  body {
    width: 1200px; height: 907px; position: relative;
    background: var(--backdrop);
    font-family: "Open Sans", sans-serif;
    color: var(--ink);
  }
  .sheet {
    position: absolute; background: var(--paper);
    box-shadow: 2px 2px 4px rgba(0,0,0,.25);
    overflow: hidden;
  }
  .brand-name {
    position: absolute; margin: 0;
    font-family: "Open Sans", sans-serif; font-weight: 400;
    color: var(--brand-blue); white-space: nowrap; line-height: 1;
  }
  .contact-list { list-style: none; margin: 0; padding: 0; position: absolute; }
  .contact-list li { display: flex; align-items: center; white-space: nowrap; }
  .contact-list svg { flex: none; fill: var(--brand-blue); }
  .band { position: absolute; left: 0; }
  .band svg { position: absolute; left: 0; top: 0; }
  .band-text {
    position: absolute; top: 0; color: #fff; white-space: nowrap;
    display: flex; align-items: center; justify-content: center;
  }

  /* Letterhead */
  .letterhead { left: 72px; top: 75px; width: 535px; height: 757px; }
  .letterhead .brand-name { left: 29px; top: 60px; font-size: 21px; }
  .letterhead .contact-list { left: 372px; top: 53px; font-size: 8.3px; line-height: 11px; color: var(--ink-soft); }
  .letterhead .contact-list svg { width: 7px; height: 7px; margin-right: 3px; }
  .letterhead .header-rule { position: absolute; left: 27px; top: 101px; width: 481px; height: 0; border-top: 0.7px solid var(--rule); }
  .letter-body { position: absolute; left: 48px; top: 233px; width: 440px; font-family: "Arimo", sans-serif; }
  .salutation { font-family: "Open Sans", sans-serif; font-weight: 600; font-size: 12px; margin: 0 0 20px; color: var(--ink); }
  .letter-body p.copy { font-size: 9.2px; line-height: 10.9px; margin: 0 0 10px; color: var(--ink-soft); }
  .sign-off { font-family: "Open Sans", sans-serif; font-weight: 600; font-size: 7px; margin: 16px 0 12px; color: var(--ink); }
  .signature-area { width: 90px; height: 28px; background: linear-gradient(90deg, #dcdcdc, #ececec); border-radius: 3px; }
  .letterhead .band { top: 713px; width: 535px; height: 26px; }
  .letterhead .band-text { left: 0; width: 535px; height: 26px; font-size: 8.6px; }

  /* Business card front */
  .card-front { left: 640px; top: 148px; width: 488px; height: 278px; }
  .card-front .brand-name { left: 35px; top: 128px; font-size: 21px; }
  .card-front .divider { position: absolute; left: 244px; top: 84px; width: 0; height: 113px; border-left: 1px solid #8a8a8a; }
  .card-front .person { position: absolute; left: 259px; top: 82px; margin: 0; line-height: 1.05; }
  .card-front .person strong { display: block; font-weight: 700; font-size: 17.5px; color: var(--brand-blue); }
  .card-front .person span { display: block; font-size: 13.5px; color: var(--ink-soft); letter-spacing: .2px; }
  .card-front .contact-list { left: 257px; top: 129px; font-size: 13px; line-height: 17px; color: var(--ink-soft); }
  .card-front .contact-list svg { width: 11px; height: 11px; margin-right: 4px; }
  .card-front .band { top: 232px; width: 488px; height: 23px; }
  .card-front .band-text { left: 0; width: 486px; height: 23px; font-size: 13.5px; }

  /* Business card back */
  .card-back { left: 640px; top: 482px; width: 488px; height: 279px; background: var(--brand-blue); }
  .card-back .brand-name { left: 0; width: 488px; text-align: center; top: 122px; font-size: 34px; color: #fff; }
</style>
</head>
<body>

<section class="sheet letterhead" aria-label="Letterhead">
  <p class="brand-name">Dr Melva Parkson</p>
  <ul class="contact-list">
    <li><svg viewBox="0 0 10 10"><path d="M1 3c0-1 1-2 4-2s4 1 4 2v1H7V3H3v1H1zM2 5h6l1 4H1z"/></svg>03 9412 7053</li>
    <li><svg viewBox="0 0 10 10"><path d="M2 1h6v3H2zM1 4h8v4H1zm2 2v3h4V6z"/></svg>03 9412 7055</li>
    <li><svg viewBox="0 0 10 10"><path d="M5 0l5 4v6H0V4zM1 4.5l4 3 4-3L5 2z"/></svg>admin@drmelvaparkson.com.au</li>
    <li><svg viewBox="0 0 10 10"><circle cx="5" cy="5" r="5"/></svg>www.drmelvaparkson.com.au</li>
  </ul>
  <div class="header-rule"></div>

  <div class="letter-body">
    <p class="salutation">Dear Mr. Dalton,</p>
    <p class="copy">Lorem ipsum dolor sit amet, consectetuer adipiscing elit, sed diam nonmmy nibh euismod tincidunt ut laor eet dolore magna aliquam erat volutpat. Ut wisi enim ad minim veniam, quis nostrud exerci tationmcorper suscipit lobortis nisl ut aliquip ex ea commodo consequat. Duis autem vel eum iriure dolor in hendrerit in vulputate velit esse molestie consequat, vel illum dolore eu feugiat</p>
    <p class="copy">Rorem ipsum dolor sit amet, consectetuer adipiscing elit, sed diam nonmmy nibh euismod tincidunt ut laor eet dolore magna aliquam erat volutpat. Ut wisi enim ad minim veniam, quis nostrud exerci tationmcorper suscipit lobortis nisl ut aliquip ex ea commodo consequat. Duis autem vel eum iriure dolor in hendrerit in vulputate velit esse molest</p>
    <p class="copy">Dorem ipsum dolor sit amet, consectetuer adipiscing elit, sed diam nonmmy nibh euismod tincidunt ut laor eet dolore magna aliquam erat volutpat. Ut wisi enim ad minim veniam, quis nostrud exerci tationmcorper suscipit lobortis nisl ut aliquip ex ea commodo consequat. Duis autem vel eum iriure dolor in hendrerit in suscipit lobortis nisl ut aliquip ex ea commodo consequat. Duis autem vel eum iriure dolor in hendrerit in vulputate velit esse molestie consequat, vel illum</p>
    <p class="copy">Sorem ipsum dolor sit amet, consectetuer adipiscing elit, sed diam nonmmy nibh euismod tincidunt ut laor eet dolore magna aliquam erat volutpat. Ut wisi enim ad minim veniam, quis nostrud exerci tationmcorper suscipit lobortis nisl ut aliquip ex ea commodo consequat. Duis autem vel eum iriure dolor in</p>
    <p class="sign-off">Sincerely,</p>
    <div class="signature-area" role="img" aria-label="Handwritten signature"></div>
  </div>

  <div class="band">
    <svg width="535" height="26" viewBox="0 0 535 26">
      <polygon points="0,0 468,0 448,26 0,26" fill="var(--brand-blue)"/>
      <polygon points="470,0 535,0 535,26 450,26" fill="var(--brand-plum)"/>
    </svg>
    <div class="band-text">Suite 4, 238 Kestrel Lane, Richmond, VIC 3121</div>
  </div>
</section>

<section class="sheet card-front" aria-label="Business card front">
  <p class="brand-name">Dr Melva Parkson</p>
  <div class="divider"></div>
  <p class="person"><strong>DR MELVA PARKSON</strong><span>ENDOCRINOLOGY</span></p>
  <ul class="contact-list">
    <li><svg viewBox="0 0 10 10"><path d="M1 3c0-1 1-2 4-2s4 1 4 2v1H7V3H3v1H1zM2 5h6l1 4H1z"/></svg>03 9412 7053</li>
    <li><svg viewBox="0 0 10 10"><path d="M2 1h6v3H2zM1 4h8v4H1zm2 2v3h4V6z"/></svg>03 9412 7055</li>
    <li><svg viewBox="0 0 10 10"><path d="M5 0l5 4v6H0V4zM1 4.5l4 3 4-3L5 2z"/></svg>admin@drmelvaparkson.com.au</li>
    <li><svg viewBox="0 0 10 10"><circle cx="5" cy="5" r="5"/></svg>www.drmelvaparkson.com.au</li>
  </ul>
  <div class="band">
    <svg width="488" height="23" viewBox="0 0 488 23">
      <polygon points="0,0 425,0 407,23 0,23" fill="var(--brand-blue)"/>
      <polygon points="428,0 488,0 488,23 410,23" fill="var(--brand-plum)"/>
    </svg>
    <div class="band-text">Suite 4, 238 Kestrel Lane, Richmond, VIC 3121</div>
  </div>
</section>

<section class="sheet card-back" aria-label="Business card back">
  <p class="brand-name">Dr Melva Parkson</p>
</section>

</body>
</html>
```